'Gravelmoth Co' Business Cards

Gravelmoth Co is a clothing company geared toward people in the mining industry who are crushing it (literally) We need a design for a business card that has 'GM' similar to the layout of the inspo photo below. Rock textures and maybe some rock dust (see GIF). I Included SVG of our circle logo but not sure how to include without it being boring, would like some ideas. Front should say 'Gravelmoth Co.' (and 'clothing' in smaller letters below) Back should have our webpage 'gravelmothco.ca' our email 'info@gravelmothco.ca' plus a FB and IG icon

```html
<!DOCTYPE html>
<html lang="en">
<head>
<meta charset="utf-8">
<title>Gravelmoth Co — Business Cards</title>
<link href="https://fonts.googleapis.com/css2?family=Archivo+Black&family=Roboto+Condensed:wght@500;700&display=swap" rel="stylesheet">
<style>
  :root {
    --backdrop: #cfccc9;
    --card: #353535;
    --card-deep: #272727;
    --band: #121212;
    --rock-light: #4a4a4a;
    --rock-mid: #333333;
    --rock-dark: #161616;
    --green: #86bc2c;
    --white: #f4f4f4;
    --muted: #b9b9b9;
  }
  * { margin: 0; padding: 0; box-sizing: border-box; }
  html, body { width: 1200px; height: 1200px; overflow: hidden; }
  body {
    position: relative;
    background: radial-gradient(circle at 25% 20%, #e2dfdc 0%, var(--backdrop) 45%, #a9a7a6 100%);
    font-family: "Roboto Condensed", sans-serif;
  }

  .card {
    position: absolute; left: 242px; width: 703px; height: 400px;
    overflow: hidden;
    box-shadow: 4px 6px 10px rgba(0,0,0,0.35);
  }
  .card--front { top: 170px; background: var(--card-deep); }
  .card--back {
    top: 629px;
    background:
      radial-gradient(ellipse at 20% 30%, rgba(255,255,255,0.05) 0%, transparent 45%),
      radial-gradient(ellipse at 75% 80%, rgba(0,0,0,0.18) 0%, transparent 50%),
      linear-gradient(160deg, #3a3a3a 0%, var(--card) 45%, var(--card-deep) 100%);
  }

  .rock-texture {
    position: absolute; left: 0; top: 0; width: 584px; height: 400px;
    background:
      radial-gradient(ellipse 150px 200px at 400px 260px, rgba(10,10,10,0.85) 0%, rgba(10,10,10,0.4) 55%, transparent 100%),
      radial-gradient(ellipse 120px 110px at 330px 110px, rgba(15,15,15,0.6) 0%, transparent 100%),
      radial-gradient(ellipse 90px 120px at 40px 60px, rgba(120,120,120,0.35) 0%, transparent 100%),
      radial-gradient(ellipse 110px 90px at 120px 370px, rgba(10,10,10,0.55) 0%, transparent 100%),
      radial-gradient(circle at 30% 50%, var(--rock-light) 0%, var(--rock-mid) 45%, var(--rock-dark) 100%);
  }
  .emblem {
    position: absolute; left: 46px; top: 74px; width: 256px; height: 256px;
    border-radius: 50%; background: var(--green);
    box-shadow:
      inset 0 0 14px rgba(0,0,0,0.45),
      0 0 0 30px #2c2c2c,
      0 0 0 36px #4a4a4a,
      0 6px 0 36px #1a1a1a;
    display: flex; align-items: center; justify-content: center;
    font-family: "Archivo Black", sans-serif; font-size: 92px; color: var(--rock-dark);
  }

  .side-band {
    position: absolute; right: 0; top: 0; width: 119px; height: 400px;
    background: linear-gradient(90deg, #0c0c0c, #1c1c1c 55%, #2a2a2a 80%, var(--band));
  }
  .side-band__lockup {
    position: absolute; left: 50%; top: 50%;
    transform: translate(-50%, -50%) rotate(-90deg);
    text-align: center; white-space: nowrap;
  }
  .wordmark { font-family: "Archivo Black", sans-serif; color: var(--white); line-height: 1; white-space: nowrap; }
  .side-band .wordmark { font-size: 31px; }
  .tagline { color: var(--muted); font-family: "Roboto Condensed", sans-serif; font-weight: 500; letter-spacing: 3px; }
  .side-band .tagline { font-size: 10px; margin-top: 6px; }

  .back-lockup {
    position: absolute; left: 54px; top: 114px; width: 216px; text-align: center;
  }
  .back-lockup__circle {
    width: 118px; height: 118px; border-radius: 50%; background: var(--white);
    margin: 0 auto 18px;
  }
  .back-lockup .wordmark { font-size: 22px; }
  .back-lockup .tagline { font-size: 9px; color: var(--white); margin-top: 4px; }

  .contact-list { position: absolute; left: 339px; top: 140px; list-style: none; }
  .contact-list li {
    display: flex; align-items: center; height: 40px;
    color: var(--white); font-weight: 700; font-size: 22px; letter-spacing: 1.8px;
  }
  .contact-icon { width: 26px; height: 26px; margin-right: 12px; flex: none; }
  .social-row { display: flex; gap: 9px; margin-top: 2px; }
  .social-dot { width: 26px; height: 26px; border-radius: 50%; background: var(--green); }
</style>
</head>
<body>
  <section class="card card--front">
    <div class="rock-texture" role="img" aria-label="Dark rock texture with shattered stone fragments and rock dust bursting outward from the emblem"></div>
    <div class="emblem">GM</div>
    <div class="side-band">
      <div class="side-band__lockup">
        <div class="wordmark">GRAVELMOTH CO</div>
        <div class="tagline">CLOTHING</div>
      </div>
    </div>
  </section>

  <section class="card card--back">
    <div class="back-lockup">
      <div class="back-lockup__circle"></div>
      <div class="wordmark">GRAVELMOTH CO</div>
      <div class="tagline">CLOTHING</div>
    </div>
    <ul class="contact-list">
      <li>
        <svg class="contact-icon" viewBox="0 0 26 26" aria-hidden="true">
          <circle cx="13" cy="13" r="13" fill="#86bc2c"/>
          <g fill="none" stroke="#333" stroke-width="1.6">
            <circle cx="13" cy="13" r="7.5"/>
            <ellipse cx="13" cy="13" rx="3.4" ry="7.5"/>
            <line x1="5.5" y1="13" x2="20.5" y2="13"/>
          </g>
        </svg>
        GRAVELMOTHCO.CA
      </li>
      <li>
        <svg class="contact-icon" viewBox="0 0 26 26" aria-hidden="true">
          <circle cx="13" cy="13" r="13" fill="#86bc2c"/>
          <rect x="6.5" y="8.5" width="13" height="9" rx="1" fill="#333"/>
          <polyline points="6.5,8.5 13,14 19.5,8.5" fill="none" stroke="#86bc2c" stroke-width="1.4"/>
        </svg>
        INFO@GRAVELMOTHCO.CA
      </li>
      <li>
        <div class="social-row" role="img" aria-label="Social media profile markers">
          <span class="social-dot"></span>
          <span class="social-dot"></span>
        </div>
      </li>
    </ul>
  </section>
</body>
</html>
```